Animal Horse & Bedding Company Needs a Website Coded & Designed

We need a website for a new animal bedding and feed company that is visually grabbing and vibrant. We would like to see a website that displays trust, quality and confidence. Needs to be responsive and mobile friendly for all browsers and coded for both Android & IOS. SEO is also important.

Joomla or Wordpress – must be both desktop and mobile friendly with fast page load speed. Need the ability to edit ourselves in Wordpress or Joomla.

Full details attached below with some layout and content ideas.

Coding

Coded - Design and coding required

Number of Pages Required

5+ page

Font styles to use
Sans Serif

Requirements
Must have
• Needs to be responsive and mobile friendly for all browsers and coded for both Android & IOS. SEO is also important.

Wordpress – must be both desktop and mobile friendly with fast page load speed. Need the ability to edit ourselves in Wordpress.

Logo Colours:
Dark Brown
CMYK: 50 / 70 / 80 / 70
Pantone: 4625C

Orange
CMYK: 0 / 50 / 100 / 0
Pantone: 144C
Nice to have
• Use picture of building attached and super impose logo on building.

```html
<!DOCTYPE html>
<html lang="en">
<head>
<meta charset="utf-8">
<title>The Hay Loft – Bedding &amp; Feed</title>
<link rel="stylesheet" href="https://fonts.googleapis.com/css2?family=Oswald:wght@400;500;600;700&family=Open+Sans:wght@400;600;700&display=swap">
<style>
:root{
  --brown:#3a2416;
  --brown-dark:#2a190f;
  --orange:#f7941d;
  --ink:#3c3c3c;
  --muted:#777;
  --light:#f2f2f2;
  --white:#fff;
}
*{box-sizing:border-box;margin:0;padding:0}
html,body{width:1200px;height:3392px;overflow:hidden}
body{font-family:"Open Sans",Arial,sans-serif;color:var(--ink);background:var(--white);position:relative}
.abs{position:absolute}
.heading{font-family:"Oswald",Arial,sans-serif;color:var(--brown);text-transform:uppercase}
.btn{display:inline-block;background:var(--brown);color:var(--white);font:600 13px "Open Sans",sans-serif;text-transform:uppercase;padding:9px 22px;border-radius:20px;letter-spacing:.5px}
svg{flex-shrink:0}

/* header */
.site-header{top:0;left:0;width:1200px;height:112px;background:var(--white)}
.brand{left:150px;top:40px;display:flex;align-items:center;gap:10px}
.brand .dot{width:18px;height:18px;border-radius:50%;background:var(--orange)}
.brand .name{font:600 22px/1 "Open Sans",sans-serif;color:var(--brown)}
.contact-bar{top:14px;right:160px;display:flex;gap:26px;font-size:13px;color:var(--ink);align-items:center}
.contact-bar span{display:flex;align-items:center;gap:6px}
.contact-bar b{font-weight:700;color:var(--brown)}
.ico{width:22px;height:22px;border-radius:50%;background:var(--brown);display:inline-flex;align-items:center;justify-content:center}
.main-nav{top:62px;right:160px;display:flex;gap:24px;align-items:center;font:600 13px "Open Sans",sans-serif;text-transform:uppercase;color:var(--brown)}
.main-nav .active{color:var(--orange);border-bottom:2px solid var(--orange);padding-bottom:4px}
.main-nav .quote{background:var(--orange);color:var(--white);padding:8px 18px;border-radius:4px}

/* hero */
.hero{top:112px;left:0;width:1200px;height:520px;background:linear-gradient(180deg,#c9d3dc 0%,#a8b4a8 30%,#6b6a3c 55%,#5c4a2a 100%)}
.hero h1{position:absolute;top:390px;left:0;width:1200px;text-align:center;font:700 44px/1.25 "Oswald",sans-serif;color:var(--white);text-shadow:0 2px 6px rgba(0,0,0,.4)}

/* features */
.features{top:700px;left:0;width:1200px;display:flex;justify-content:center;gap:86px}
.feature{width:230px;text-align:center}
.diamond{width:130px;height:130px;margin:20px auto 44px;transform:rotate(45deg);border-radius:18px;border:4px solid var(--brown);display:flex;align-items:center;justify-content:center;background:var(--white);box-shadow:0 0 0 8px var(--white),0 0 0 10px #ddd}
.diamond.hot{background:var(--orange);border-color:var(--orange)}
.diamond .inner{transform:rotate(-45deg);width:74px;height:74px;border-radius:50%;background:var(--brown);display:flex;align-items:center;justify-content:center}
.diamond.hot .inner{background:var(--white)}
.feature h3{font:600 15px "Oswald",sans-serif;text-transform:uppercase;color:var(--brown);margin-bottom:8px}
.feature p{font-size:11.5px;line-height:1.55;color:var(--muted)}

/* about */
.about-photo{top:1190px;left:0;width:610px;height:400px;background:linear-gradient(135deg,#c8c4bd,#8c7f72 50%,#5a4a3c)}
.about-box{top:1255px;left:580px;width:460px;height:390px;background:var(--orange);padding:48px 36px;color:var(--white)}
.about-box h2{font:600 24px "Oswald",sans-serif;text-transform:uppercase;margin-bottom:8px}
.about-box .rule{width:50px;height:3px;background:var(--white);margin-bottom:22px}
.about-box p{font-size:13px;line-height:1.65;margin-bottom:14px}
.about-box .btn{margin-top:10px}

/* bedding */
.bedding-photo{top:1830px;left:160px;width:420px;height:420px;border-radius:50%;background:radial-gradient(circle at 45% 40%,#c98a4e,#8a5a2e 55%,#3f5a2a)}
.bedding{top:1840px;left:625px;width:420px}
.bedding h2{font-size:30px;font-weight:600;margin-bottom:20px}
.checklist{list-style:none}
.checklist li{display:flex;align-items:center;gap:10px;font-size:14px;line-height:1.2;margin-bottom:15px}
.bedding .btn{margin-top:12px}

/* feed */
.feed{top:2370px;left:0;width:1200px;text-align:center}
.feed h2{font-size:32px;font-weight:600;margin-bottom:16px}
.feed .intro{width:820px;margin:0 auto 34px;font-size:12.5px;line-height:1.6;color:var(--muted)}
.feed-cols{display:flex;justify-content:center;gap:70px;text-align:left}
.feed-cols ul{list-style:none;width:230px}
.feed-cols li{display:flex;gap:10px;font-size:14px;margin-bottom:18px;align-items:flex-start}
.feed .btn{margin-top:40px}

/* newsletter */
.newsletter{top:2820px;left:0;width:1200px;height:290px;background:var(--light)}
.newsletter h2{position:absolute;left:255px;top:110px;font:600 30px/1.15 "Oswald",sans-serif;color:var(--brown);text-align:right;text-transform:uppercase}
.newsletter .divider{position:absolute;left:480px;top:105px;width:2px;height:85px;background:#ccc}
.newsletter .sub{position:absolute;left:515px;top:118px;font-size:12px;color:var(--muted)}
.newsletter .field{position:absolute;left:515px;top:146px;width:340px;height:36px;border:1px solid #ccc;background:var(--white);border-radius:18px;font-size:12px;color:#999;padding:10px 18px}
.newsletter .btn{position:absolute;left:862px;top:146px;height:36px;padding:10px 22px}

/* footer */
.site-footer{top:3110px;left:0;width:1200px;height:245px;background:linear-gradient(180deg,#4a2e1c,var(--brown-dark))}
.site-footer .brand{top:108px}
.site-footer .brand .name{color:var(--white)}
.foot-items{position:absolute;top:60px;left:470px;display:flex;gap:90px}
.foot-item{width:130px;text-align:center;color:var(--white);font-size:12px;line-height:1.4}
.foot-item .circle{width:54px;height:54px;border-radius:50%;background:var(--orange);margin:0 auto 12px;display:flex;align-items:center;justify-content:center}
.foot-item b{display:block;font:600 22px "Oswald",sans-serif}
.copy{top:3355px;left:0;width:1200px;height:37px;background:#1f120a;color:#bbb;font-size:11px;padding:12px 160px;display:flex;justify-content:space-between}
.social{display:flex;gap:6px}
.social i{width:16px;height:16px;border-radius:50%;background:#3a6fb5;display:block}
</style>
</head>
<body>

<header class="site-header abs">
  <div class="brand abs">
    <span class="dot"></span>
    <span class="name">The Hay Loft</span>
  </div>
  <div class="contact-bar abs">
    <span><i class="ico"><svg width="12" height="12" viewBox="0 0 24 24"><path fill="#fff" d="M6.6 10.8a15 15 0 0 0 6.6 6.6l2.2-2.2c.3-.3.7-.4 1-.2 1.1.4 2.3.6 3.6.6.6 0 1 .4 1 1V20c0 .6-.4 1-1 1A17 17 0 0 1 3 4c0-.6.4-1 1-1h3.5c.6 0 1 .4 1 1 0 1.3.2 2.5.6 3.6.1.3 0 .7-.2 1z"/></svg></i>Phone: <b>123 456 7890</b></span>
    <span><i class="ico"><svg width="12" height="12" viewBox="0 0 24 24"><path fill="#fff" d="M3 5h18v14H3z M3 5l9 7 9-7" stroke="#3a2416" stroke-width="1.5"/></svg></i>Email: info@thehayloft.com</span>
  </div>
  <nav class="main-nav abs">
    <span class="active">Home</span><span>About</span><span>Feed</span><span>Bedding</span><span>Contact Us</span><span class="quote">Request Quote</span>
  </nav>
</header>

<section class="hero abs" role="img" aria-label="Horses grazing in an open pasture with mountains behind">
  <h1>Your Animal Deserves The Very Best In Health And<br>Comfort To Keep Them Healthy, Strong And Happy.</h1>
</section>

<section class="features abs">
  <div class="feature">
    <div class="diamond"><div class="inner"><svg width="36" height="36" viewBox="0 0 24 24"><circle cx="12" cy="10" r="6" fill="none" stroke="#fff" stroke-width="2"/><path d="M8 15l-2 7 6-3 6 3-2-7" fill="none" stroke="#fff" stroke-width="2"/></svg></div></div>
    <h3>Quality Guaranteed</h3>
    <p>Grown for quality – 100% natural with no chemicals or additives in every bale.</p>
  </div>
  <div class="feature">
    <div class="diamond hot"><div class="inner"><svg width="36" height="36" viewBox="0 0 24 24"><circle cx="12" cy="8" r="4" fill="none" stroke="#f7941d" stroke-width="2"/><path d="M3 18c3 0 5-3 9-3h5l-4 3h-3" fill="none" stroke="#f7941d" stroke-width="2"/></svg></div></div>
    <h3>Full Service Solution</h3>
    <p>Dedicated to providing a full service solution of bedding supply and waste removal.</p>
  </div>
  <div class="feature">
    <div class="diamond"><div class="inner"><svg width="36" height="36" viewBox="0 0 24 24"><circle cx="12" cy="12" r="8" fill="none" stroke="#fff" stroke-width="2"/><path d="M8 12l3 3 5-6" fill="none" stroke="#fff" stroke-width="2"/></svg></div></div>
    <h3>Convenient &amp; Cost Effective</h3>
    <p>Compressed bags – pallets or bulk products saving in shipping costs.</p>
  </div>
</section>

<div class="about-photo abs" role="img" aria-label="Horse eating from a round hay feeder in a winter paddock"></div>
<section class="about-box abs">
  <h2>The Hay Loft About</h2>
  <div class="rule"></div>
  <p>The Hay Loft is a locally owned company located in the prairies. We are dedicated to providing high quality products and services.</p>
  <p>Producing, baling and marketing hay and straw for a number of years. Grown with care for every farm and stable.</p>
  <span class="btn">Request Quote</span>
</section>

<div class="bedding-photo abs" role="img" aria-label="Foal and mare resting on straw bedding"></div>
<section class="bedding abs">
  <h2 class="heading">Bedding Benefits</h2>
  <ul class="checklist">
    <li><svg width="16" height="16" viewBox="0 0 24 24"><path d="M4 12l5 5 11-11" fill="none" stroke="#f7941d" stroke-width="3"/></svg>100% Natural Chopped Straw</li>
    <li><svg width="16" height="16" viewBox="0 0 24 24"><path d="M4 12l5 5 11-11" fill="none" stroke="#f7941d" stroke-width="3"/></svg>Low Dust</li>
    <li><svg width="16" height="16" viewBox="0 0 24 24"><path d="M4 12l5 5 11-11" fill="none" stroke="#f7941d" stroke-width="3"/></svg>Chemical &amp; Additive Free</li>
    <li><svg width="16" height="16" viewBox="0 0 24 24"><path d="M4 12l5 5 11-11" fill="none" stroke="#f7941d" stroke-width="3"/></svg>Clean &amp; Highly Absorbent</li>
    <li><svg width="16" height="16" viewBox="0 0 24 24"><path d="M4 12l5 5 11-11" fill="none" stroke="#f7941d" stroke-width="3"/></svg>Cheaper than Wood Shavings</li>
    <li><svg width="16" height="16" viewBox="0 0 24 24"><path d="M4 12l5 5 11-11" fill="none" stroke="#f7941d" stroke-width="3"/></svg>Economic – less used and less wasted</li>
    <li><svg width="16" height="16" viewBox="0 0 24 24"><path d="M4 12l5 5 11-11" fill="none" stroke="#f7941d" stroke-width="3"/></svg>Environmentally Friendly – Recyclable &amp; Compostable</li>
  </ul>
  <span class="btn">Know More</span>
</section>

<section class="feed abs">
  <h2 class="heading">Our Feed Benefits</h2>
  <p class="intro">Hay cubes and pellets are made from premium hay, offering a variety of animals a feed that is non-GMO and packed with natural nutrients. These pellets and cubes are easy to handle, store and ship, so every bag reduces the amount of wasted feed.</p>
  <div class="feed-cols">
    <ul>
      <li><svg width="16" height="16" viewBox="0 0 24 24"><path d="M4 12l5 5 11-11" fill="none" stroke="#f7941d" stroke-width="3"/></svg>100% Natural</li>
      <li><svg width="16" height="16" viewBox="0 0 24 24"><path d="M4 12l5 5 11-11" fill="none" stroke="#f7941d" stroke-width="3"/></svg>Chemical &amp; Additive Free</li>
      <li><svg width="16" height="16" viewBox="0 0 24 24"><path d="M4 12l5 5 11-11" fill="none" stroke="#f7941d" stroke-width="3"/></svg>Available in Pellets or Cubes</li>
    </ul>
    <ul>
      <li><svg width="16" height="16" viewBox="0 0 24 24"><path d="M4 12l5 5 11-11" fill="none" stroke="#f7941d" stroke-width="3"/></svg>High Protein Content</li>
      <li><svg width="16" height="16" viewBox="0 0 24 24"><path d="M4 12l5 5 11-11" fill="none" stroke="#f7941d" stroke-width="3"/></svg>Eliminate Waste in Feeding</li>
      <li><svg width="16" height="16" viewBox="0 0 24 24"><path d="M4 12l5 5 11-11" fill="none" stroke="#f7941d" stroke-width="3"/></svg>Convenient</li>
    </ul>
    <ul>
      <li><svg width="16" height="16" viewBox="0 0 24 24"><path d="M4 12l5 5 11-11" fill="none" stroke="#f7941d" stroke-width="3"/></svg>Clean – Eliminates Dust From Feeding Baled Hay</li>
      <li><svg width="16" height="16" viewBox="0 0 24 24"><path d="M4 12l5 5 11-11" fill="none" stroke="#f7941d" stroke-width="3"/></svg>Less wasted feed</li>
    </ul>
  </div>
  <span class="btn">Our Feed</span>
</section>

<section class="newsletter abs">
  <h2>Newsletter<br>Sign Up</h2>
  <div class="divider"></div>
  <p class="sub">Subscribe to our newsletter to get the latest updates in your inbox</p>
  <div class="field">Enter your email address</div>
  <span class="btn">Subscribe</span>
</section>

<footer class="site-footer abs">
  <div class="brand abs">
    <span class="dot"></span>
    <span class="name">The Hay Loft</span>
  </div>
  <div class="foot-items">
    <div class="foot-item"><div class="circle"><svg width="22" height="22" viewBox="0 0 24 24"><path fill="#fff" d="M12 2a7 7 0 0 0-7 7c0 5 7 13 7 13s7-8 7-13a7 7 0 0 0-7-7zm0 9.5a2.5 2.5 0 1 1 0-5 2.5 2.5 0 0 1 0 5z"/></svg></div>Delivery in Canada<br>&amp; USA</div>
    <div class="foot-item"><div class="circle"><svg width="22" height="22" viewBox="0 0 24 24"><path fill="#fff" d="M6.6 10.8a15 15 0 0 0 6.6 6.6l2.2-2.2c.3-.3.7-.4 1-.2 1.1.4 2.3.6 3.6.6.6 0 1 .4 1 1V20c0 .6-.4 1-1 1A17 17 0 0 1 3 4c0-.6.4-1 1-1h3.5c.6 0 1 .4 1 1 0 1.3.2 2.5.6 3.6.1.3 0 .7-.2 1z"/></svg></div>PHONE<b>123 456 7890</b></div>
    <div class="foot-item"><div class="circle"><svg width="22" height="22" viewBox="0 0 24 24"><rect x="3" y="5" width="18" height="14" fill="#fff"/><path d="M3 5l9 7 9-7" fill="none" stroke="#f7941d" stroke-width="1.5"/></svg></div>EMAIL<br>info@thehayloft.com</div>
  </div>
</footer>
<div class="copy abs">
  <span>Copyright 2021. The Hay Loft Animal Feed All Rights Reserved | Site map</span>
  <span class="social"><i></i><i></i><i></i><i></i></span>
</div>

</body>
</html>
```